Cosmetic Surgery Practice Advertising brochures

Our practice needs a brochure containing general information and procedures we offer for advertising and marketing purposes.

Our website is currently being revamped but older version is available www.verandaaesthetic.example

Our one of a kind Cosmetic Surgery Practice is second to none in southern Louisiana. Clients come to our practice from all over the country in seek of our top notch care where we seek to find a beauty that is unique to you! Everyone who walks through the doors is treated as an A list celebrity from the complementary consultation, to the walk-in walk-out surgery that is performed here in our facility under Local anesthesia. That is some of the key differences here at Rosewick:

In facility procedures = one up front all inclusive pricing. Consultations are complementary and you will meet with the Doctor himself.
No general sedation, rather local and deep sedation= walk out afterwards.
Quality of care is incomparable, patients given our cell phone numbers.

We offer Breast Augmentations, Tummy Tucks, Face procedures including neck, face, eyelid, brow lifts, etc, breast augmentations both implants and lift/reduction and liposuction with & without fat transfers to buttock or cheecks.

Most Cosmetic Surgeons typically have a specialty based practice from which they build from, like a Dermatology or ENT practice. Because our surgeon is a General Surgeon, he does not have a routine relationship client base, and must attract new patients organically. Other physicians that do not offer Cosmetic surgery services to relevantly related client base, therefore need to refer out to a surgeon that does.

Target Market(s)

Women interested in anesthetics, beauty, looking to feel their best

Industry/Entity Type

Cosmetic

Font styles to use
Serif
Script

Requirements
Must have
• Doctor Bio, Map, logo
Nice to have
• Beautiful women, CREATIVITY and ORIGINALITY
Should not have
• Harsh lines

```html
<!DOCTYPE html>
<html lang="en">
<head>
<meta charset="utf-8">
<title>Rosewick Center for Cosmetic Surgery – Brochure Outside</title>
<link rel="stylesheet" href="https://fonts.googleapis.com/css2?family=Playfair+Display:wght@400;700&family=Open+Sans:wght@400;600;700&display=swap">
<style>
  :root{
    --slate:#5f6f82;
    --slate-dark:#3f4955;
    --slate-light:#8593a3;
    --orange:#e8912f;
    --ink:#2f3740;
    --muted:#6b7480;
    --paper:#ffffff;
    --backdrop:#e9ebee;
    --leaf:#3f5a48;
  }
  *{box-sizing:border-box;margin:0;padding:0}
  html,body{width:742px;height:1200px;overflow:hidden;background:var(--backdrop)}
  body{position:relative;font-family:"Open Sans",Arial,sans-serif;color:var(--ink)}

  .brochure{position:absolute;left:21px;top:330px;width:700px;height:540px;background:var(--paper);
    display:flex;box-shadow:0 4px 18px rgba(40,50,60,.15)}
  .panel{position:relative;width:233.33px;height:100%;overflow:hidden}

  /* back panel: doctor bio */
  .bio-header{height:118px;background:var(--slate);padding:12px 12px;position:relative}
  .bio-header .faint-title{font-family:"Playfair Display",Georgia,serif;font-weight:700;color:rgba(255,255,255,.3);
    font-size:15px;line-height:1.15;text-transform:uppercase;letter-spacing:.5px;white-space:nowrap}
  .doctor-photo{position:absolute;left:50%;top:66px;transform:translateX(-50%);width:92px;height:92px;border-radius:50%;
    border:4px solid var(--orange);background:radial-gradient(circle at 50% 40%,#b9a08f 0%,#6f5f55 55%,#3c4148 100%);
    box-shadow:0 0 0 3px #fff}
  .doctor-name{margin-top:48px;text-align:center;font-family:"Playfair Display",Georgia,serif;font-weight:700;
    font-size:14px;color:var(--slate-dark);letter-spacing:.5px}
  .doctor-cred{text-align:center;font-size:6.5px;color:var(--orange);font-weight:600;letter-spacing:1px;margin-top:2px}
  .bio-text{padding:8px 18px 0;font-size:6px;line-height:1.55;color:var(--muted);text-align:justify}
  .bio-text p+p{margin-top:5px}
  .credentials{list-style:none;padding:8px 18px 0}
  .credentials li{font-size:6px;line-height:1.5;color:var(--ink);padding-left:9px;position:relative;margin-bottom:2.5px}
  .credentials li::before{content:"";position:absolute;left:0;top:2.5px;width:4px;height:4px;border-radius:50%;background:var(--orange)}

  .foot-bar{position:absolute;left:0;bottom:0;width:100%;height:20px;display:flex;align-items:center;justify-content:center;
    font-size:6px;color:#fff;letter-spacing:.6px;text-transform:uppercase;font-weight:600;white-space:nowrap}
  .foot-bar.dark{background:var(--slate-dark)}
  .foot-bar.accent{background:var(--orange)}
  .foot-bar.slate{background:var(--slate)}

  /* middle panel: testimonials & contact */
  .portrait-band{height:118px;background:linear-gradient(135deg,#dfe3e8 0%,#c9d0d8 100%);position:relative}
  .portrait-band .portrait{position:absolute;right:22px;top:8px;width:96px;height:110px;
    background:linear-gradient(180deg,#c98f5a 0%,#e7c7b2 55%,#6c86a8 100%);border-radius:2px}
  .quote{padding:12px 22px 0;text-align:center}
  .quote-mark{font-family:"Playfair Display",Georgia,serif;font-size:26px;color:var(--slate-light);line-height:.8}
  .quote p{font-size:6px;line-height:1.55;color:var(--muted);margin-top:3px}
  .quote p.highlight{color:var(--orange);font-style:italic}
  .quote .rule{width:40px;height:1px;background:#d6dbe1;margin:8px auto 0}
  .brand-small{margin-top:14px;text-align:center}
  .brand-name{font-family:"Playfair Display",Georgia,serif;font-weight:700;color:var(--slate-dark)}
  .brand-small .brand-name{font-size:17px}
  .brand-sub{font-size:5.5px;letter-spacing:1px;color:var(--slate);text-transform:uppercase;margin-top:1px}
  .contact{text-align:center;margin-top:12px}
  .contact h3{font-family:"Playfair Display",Georgia,serif;font-size:12px;color:var(--slate-dark);font-weight:700}
  .contact .note{font-size:5.5px;color:var(--orange);margin-top:3px}
  .contact .lines{font-size:6px;line-height:1.6;color:var(--muted);margin-top:6px}
  .map-pin{display:block;margin:6px auto 0}

  /* front cover */
  .cover-photo{position:absolute;inset:0 0 140px 0;
    background:linear-gradient(160deg,#f2f2f0 0%,#e9d3c6 45%,#d8b8a4 70%,#eef0ee 100%)}
  .cover-leaf{position:absolute;left:0;top:30px;width:80px;height:260px;
    background:linear-gradient(180deg,var(--leaf) 0%,#5f7d66 100%);opacity:.75;border-radius:0 80px 80px 0}
  .cover-curve{position:absolute;left:0;bottom:20px;width:100%;height:200px}
  .cover-brand{position:absolute;left:0;right:0;bottom:68px;text-align:center}
  .cover-brand .brand-name{font-size:32px}
  .cover-brand .brand-sub{font-size:7px;margin-top:3px}
  .cover-tag{position:absolute;right:14px;top:290px;width:110px;font-size:6.5px;line-height:1.5;color:var(--slate-dark);text-align:right}
</style>
</head>
<body>
<main class="brochure">

  <section class="panel panel-bio">
    <header class="bio-header">
      <div class="faint-title">Rosewick Center<br>for Cosmetic Surgery</div>
    </header>
    <div class="doctor-photo" role="img" aria-label="Portrait photograph of the surgeon"></div>
    <h2 class="doctor-name">DANIEL OKAFOR</h2>
    <div class="doctor-cred">MD</div>
    <div class="bio-text">
      <p>Our founder, Dr. Daniel Okafor, MD, is a board certified general surgeon who has focused on cosmetic surgery for more than a decade, with over twenty years of surgical practice.</p>
      <p>He personally meets every patient and performs each procedure in our own facility, with a calm, caring approach to your goals.</p>
    </div>
    <ul class="credentials">
      <li>Board certified general surgeon</li>
      <li>Advanced training in cosmetic surgery</li>
      <li>Fellowship trained in body contouring</li>
      <li>Specialist in facial rejuvenation</li>
      <li>Experienced in breast procedures</li>
      <li>General surgical practice over 20 years</li>
      <li>Cosmetic surgical practice over 10 years</li>
      <li>Self taught artist</li>
    </ul>
    <div class="foot-bar dark">Mail us: www.verandaaesthetic.example</div>
  </section>

  <section class="panel panel-contact">
    <div class="portrait-band">
      <div class="portrait" role="img" aria-label="Photograph of a smiling patient"></div>
    </div>
    <div class="quote">
      <div class="quote-mark">&ldquo;</div>
      <p>I could not be more pleased with my results. From the very first visit I felt cared for, and the team answered every question.</p>
      <p class="highlight">Sarah M.</p>
      <div class="rule"></div>
      <p>Walking out the same day was easier than I ever imagined. Everyone treated me like family and I recommend them to all my friends.</p>
      <p class="highlight">Ashley R.</p>
    </div>
    <div class="brand-small">
      <div class="brand-name">Rosewick</div>
      <div class="brand-sub">Center for Cosmetic Surgery</div>
    </div>
    <div class="contact">
      <h3>Contact Us Today</h3>
      <div class="note">Your consultation is complimentary</div>
      <svg class="map-pin" width="9" height="12" viewBox="0 0 9 12" aria-hidden="true">
        <path d="M4.5 0C2 0 0 2 0 4.5 0 7.8 4.5 12 4.5 12S9 7.8 9 4.5C9 2 7 0 4.5 0z" fill="var(--orange)"/>
        <circle cx="4.5" cy="4.5" r="1.7" fill="#fff"/>
      </svg>
      <div class="lines">4820 Magnolia Crest Blvd, Suite 210<br>Cypress Landing, LA 00000<br>(555) 010-2846</div>
    </div>
    <div class="foot-bar accent">Visit us: www.verandaaesthetic.example</div>
  </section>

  <section class="panel panel-cover">
    <div class="cover-photo" role="img" aria-label="Photograph of a woman with glowing skin beside tropical leaves"></div>
    <div class="cover-leaf" role="img" aria-label="Tropical leaf photograph"></div>
    <svg class="cover-curve" viewBox="0 0 233 200" preserveAspectRatio="none" aria-hidden="true">
      <path d="M0 60 Q 110 10 233 40 L233 200 L0 200 Z" fill="#fff"/>
      <path d="M0 60 Q 110 10 233 40" fill="none" stroke="var(--slate-light)" stroke-width="1.2"/>
    </svg>
    <div class="cover-tag">Rosewick is a free-standing facility that offers the latest in Cosmetic Surgery.</div>
    <div class="cover-brand">
      <div class="brand-name">Rosewick</div>
      <div class="brand-sub">Center for Cosmetic Surgery</div>
    </div>
    <div class="foot-bar slate">Call us: (555) 010-2846</div>
  </section>

</main>
</body>
</html>
```